Stationary Design for Stunning new Logo

I need to envelopes, letterhead, business cards designed to compliment our new logo.

We are a 25 year old printing company going through a brand refresh. All items should have the design extended to both sides for full print ability.

Industry/Entity Type

Printing

Requirements
Must have
• It must utilize the new logo & colors PMS 300 & PMS 295.

```html
<!DOCTYPE html>
<html lang="en">
<head>
<meta charset="utf-8">
<title>NOVAPRINT Stationery Set</title>
<link rel="stylesheet" href="https://fonts.googleapis.com/css2?family=Arimo:wght@400;700&family=Roboto+Condensed:wght@400&display=swap">
<style>
  :root {
    --pms300: #0a66c8;
    --pms295: #0b2f66;
    --paper: #ffffff;
    --stage: #e4e4e4;
    --ink: #1a1a1a;
    --shadow: 0 3px 6px rgba(0,0,0,0.45);
  }
  * { box-sizing: border-box; margin: 0; padding: 0; }
  html, body { width: 1200px; height: 857px; overflow: hidden; }
  body {
    background: linear-gradient(180deg, #d6d6d6 0%, #ececec 50%, #d9d9d9 100%);
    font-family: "Arimo", Arial, sans-serif;
    color: var(--ink);
    position: relative;
  }
  .piece { position: absolute; background: var(--paper); box-shadow: var(--shadow); overflow: hidden; }

  /* brand lockup */
  .brand { position: absolute; display: flex; align-items: center; gap: 6px; }
  .brand-dot { border-radius: 50%; background: var(--pms300); flex: none; }
  .brand-name { font-family: "Arimo", Arial, sans-serif; font-weight: 700; color: var(--pms300); letter-spacing: 1px; line-height: 1; }
  .brand-tagline { font-family: "Roboto Condensed", "Arial Narrow", sans-serif; color: var(--pms300); white-space: nowrap; line-height: 1; margin-top: 3px; }
  .brand.on-blue .brand-dot { background: #ffffff; }
  .brand.on-blue .brand-name { color: #ffffff; }
  .brand.on-blue .brand-tagline { color: #dfe8f5; }

  .pattern-field {
    position: absolute; inset: 0;
    background: linear-gradient(180deg, #0d5fc4 0%, #1a6fd4 45%, #0b56b5 100%);
  }

  /* letterhead */
  .letterhead { left: 9px; top: 29px; width: 441px; height: 612px; box-shadow: none; }
  .letterhead .brand { left: 19px; top: 27px; }
  .sender { position: absolute; left: 326px; top: 25px; }
  .sender-name { font-size: 12px; font-weight: 700; color: var(--pms295); }
  .sender-title { font-size: 12px; font-weight: 700; color: var(--pms300); }
  .sender-address { font-size: 5.5px; font-weight: 700; color: var(--pms295); margin-top: 4px; white-space: nowrap; }
  .contact-row { position: absolute; display: flex; align-items: center; gap: 6px; font-size: 9px; font-weight: 700; color: var(--pms295); }
  .icon { flex: none; display: block; }

  /* backing sheet */
  .sheet-back { left: 738px; top: 5px; width: 453px; height: 636px; }
  .sheet-back .brand { left: 56px; top: 576px; }

  /* business card front */
  .card-front { left: 410px; top: 120px; width: 379px; height: 216px; }
  .card-front .brand { left: 92px; top: 168px; }

  /* business card back */
  .card-back { left: 411px; top: 360px; width: 377px; height: 214px; }
  .card-holder { position: absolute; right: 24px; top: 24px; text-align: center; line-height: 1.05; }
  .card-holder-name { font-size: 15px; font-weight: 700; color: var(--pms300); }
  .card-holder-title { font-size: 14px; font-weight: 700; color: var(--pms295); }
  .card-back .brand { left: 69px; top: 80px; }
  .card-rule { position: absolute; left: 0; right: 0; top: 145px; height: 9px; background: var(--pms300); }
  .card-icon { position: absolute; top: 137px; }
  .card-contact {
    position: absolute; top: 168px; width: 120px;
    font-size: 10px; color: var(--ink); white-space: nowrap; text-align: center;
  }
  .card-footer {
    position: absolute; left: 0; right: 0; bottom: 0; height: 21px;
    background: var(--pms295); color: #fff; font-size: 10.5px; font-weight: 700;
    display: flex; align-items: center; justify-content: center; padding-right: 24px;
  }
  .card-footer-notch { position: absolute; right: 40px; top: 193px; }

  /* envelopes */
  .envelope-back { left: 75px; top: 650px; width: 500px; height: 195px; }
  .envelope-flap { position: absolute; left: 0; right: 0; top: 0; height: 48px; background: var(--pms300); }
  .envelope-flap .brand-dot { position: absolute; left: 239px; top: 7px; width: 30px; height: 30px; background: #fff; border-radius: 50%; }
  .envelope-front { left: 618px; top: 651px; width: 500px; height: 196px; }
  .envelope-front .brand { left: 16px; top: 22px; }
  .return-address { position: absolute; left: 17px; top: 162px; font-size: 8.5px; font-weight: 700; color: var(--pms295); line-height: 1.4; }
</style>
</head>
<body>

<!-- Letterhead -->
<section class="piece letterhead" aria-label="Letterhead">
  <div class="brand">
    <span class="brand-dot" style="width:30px;height:30px"></span>
    <div>
      <div class="brand-name" style="font-size:25px">NOVAPRINT</div>
      <div class="brand-tagline" style="font-size:7.5px">OUTSTANDING SERVICE • QUALITY PRODUCT • COMPETITIVE PRICING.</div>
    </div>
  </div>
  <div class="sender">
    <div class="sender-name">YOUR NAME</div>
    <div class="sender-title">TITLE</div>
    <div class="sender-address">NOVAPRINT. P.O.BOX 1234 TX 1234</div>
  </div>
  <div class="contact-row" style="left:19px;top:590px">
    <svg class="icon" width="20" height="20" viewBox="0 0 20 20"><circle cx="10" cy="10" r="10" fill="var(--pms300)"/><path d="M5 9c0-2 2-3 5-3s5 1 5 3l-2 .5-.5-1.5h-5L7 9.5z M7 10h6l1 4H6z" fill="#fff"/></svg>
    <span>123456789</span>
  </div>
  <div class="contact-row" style="left:150px;top:590px">
    <svg class="icon" width="20" height="20" viewBox="0 0 20 20"><circle cx="10" cy="10" r="10" fill="var(--pms300)"/><rect x="5" y="6.5" width="10" height="7" fill="#fff"/><path d="M5 6.5l5 4 5-4" fill="none" stroke="var(--pms300)" stroke-width="1"/></svg>
    <span>yourname@novaprint.com</span>
  </div>
  <div class="contact-row" style="left:316px;top:590px">
    <svg class="icon" width="20" height="20" viewBox="0 0 20 20"><circle cx="10" cy="10" r="10" fill="var(--pms300)"/><g fill="none" stroke="#fff" stroke-width="1"><circle cx="10" cy="10" r="5.5"/><ellipse cx="10" cy="10" rx="2.5" ry="5.5"/><path d="M4.5 10h11M5.5 7h9M5.5 13h9"/></g></svg>
    <span>www.novaprint.com</span>
  </div>
</section>

<!-- Reverse sheet -->
<section class="piece sheet-back" aria-label="Letterhead reverse">
  <div class="pattern-field" role="img" aria-label="Repeating brand pattern in blue tones"></div>
  <div class="brand on-blue">
    <span class="brand-dot" style="width:40px;height:40px"></span>
    <div>
      <div class="brand-name" style="font-size:34px">NOVAPRINT</div>
      <div class="brand-tagline" style="font-size:10.5px">OUTSTANDING SERVICE • QUALITY PRODUCT • COMPETITIVE PRICING.</div>
    </div>
  </div>
</section>

<!-- Business card front -->
<section class="piece card-front" aria-label="Business card front">
  <div class="pattern-field" role="img" aria-label="Repeating brand pattern in blue tones"></div>
  <div class="brand on-blue">
    <span class="brand-dot" style="width:34px;height:34px"></span>
    <div>
      <div class="brand-name" style="font-size:28px">NOVAPRINT</div>
      <div class="brand-tagline" style="font-size:8px">OUTSTANDING SERVICE • QUALITY PRODUCT • COMPETITIVE PRICING.</div>
    </div>
  </div>
</section>

<!-- Business card back -->
<section class="piece card-back" aria-label="Business card back">
  <div class="card-holder">
    <div class="card-holder-name">YOUR NAME</div>
    <div class="card-holder-title">Title</div>
  </div>
  <div class="brand">
    <span class="brand-dot" style="width:30px;height:30px"></span>
    <div>
      <div class="brand-name" style="font-size:25px">NOVAPRINT</div>
      <div class="brand-tagline" style="font-size:7px">OUTSTANDING SERVICE • QUALITY PRODUCT • COMPETITIVE PRICING.</div>
    </div>
  </div>
  <div class="card-rule"></div>
  <svg class="card-icon" style="left:64px" width="26" height="26" viewBox="0 0 20 20"><circle cx="10" cy="10" r="10" fill="var(--pms300)"/><path d="M5 9c0-2 2-3 5-3s5 1 5 3l-2 .5-.5-1.5h-5L7 9.5z M7 10h6l1 4H6z" fill="#fff"/></svg>
  <svg class="card-icon" style="left:176px" width="26" height="26" viewBox="0 0 20 20"><circle cx="10" cy="10" r="10" fill="var(--pms300)"/><rect x="5" y="6.5" width="10" height="7" fill="#fff"/><path d="M5 6.5l5 4 5-4" fill="none" stroke="var(--pms300)" stroke-width="1"/></svg>
  <svg class="card-icon" style="left:285px" width="26" height="26" viewBox="0 0 20 20"><circle cx="10" cy="10" r="10" fill="var(--pms300)"/><g fill="none" stroke="#fff" stroke-width="1"><circle cx="10" cy="10" r="5.5"/><ellipse cx="10" cy="10" rx="2.5" ry="5.5"/><path d="M4.5 10h11M5.5 7h9M5.5 13h9"/></g></svg>
  <div class="card-contact" style="left:16px">123 456 789</div>
  <div class="card-contact" style="left:133px">yourname@novaprint.com</div>
  <div class="card-contact" style="left:250px">www.novaprint.com</div>
  <div class="card-footer">Postal Address: NOVAPRINT. P.O.BOX 1234 TX 1234</div>
  <svg class="card-footer-notch" width="12" height="8" viewBox="0 0 12 8"><path d="M0 0h12L6 8z" fill="#fff"/></svg>
</section>

<!-- Envelope reverse -->
<section class="piece envelope-back" aria-label="Envelope reverse">
  <div class="envelope-flap"><span class="brand-dot"></span></div>
</section>

<!-- Envelope front -->
<section class="piece envelope-front" aria-label="Envelope front">
  <div class="brand">
    <span class="brand-dot" style="width:28px;height:28px"></span>
    <div>
      <div class="brand-name" style="font-size:23px">NOVAPRINT</div>
      <div class="brand-tagline" style="font-size:6.5px">OUTSTANDING SERVICE • QUALITY PRODUCT • COMPETITIVE PRICING.</div>
    </div>
  </div>
  <div class="return-address">NOVAPRINT. P.O.BOX 1234 &nbsp;TX 1234<br>www.novaprint.com</div>
</section>

</body>
</html>
```